Award Winning Production Company Needs Poster for Lastest Film

Nothing’s Amiss Pictures is looking for a movie poster for our short film "Refrain" to be used at film festivals. Refrain is a short film about a pair of StreamNook stars named Hazel and Juniper who write and perform songs together. Juniper is moving to a new city and Hazel comes to visit and see her new apartment. The film is shot in one shot as if it is livestream Juniper is hosting where she is giving Hazel and their followers a tour of the new living space. As the tour progresses Hazel begins to see that Juniper is starting to move on without her and tension builds between the two of them.

Along with a trailer, we’ve included some photos to potentially base your posters on but don't restrict yourself to just using them. You are free to use whatever elements you want! It is not required that you use the provided photos and we encourage creativity with other elements as well.

Target Market(s)

Film Festival Attendees, Milennials

Industry/Entity Type

Film Production

Requirements
Must have
• Please include these credits on the poster:
• Our company: Nothing’s Amiss Pictures
• Our stars names: Marisa Pellwright and Tamsin Kowalcek
• Directed by Dale and Brent Ushworth
• Story by Jem Ushworth
• Original Music by Marisa Pellwright
Nice to have
• We are currently debating amongst ourselves between two titles: “Refrain” and “Hazel Shows Juniper’s Fresh Loft!” You can submit posters using either title or both.

```html
<!DOCTYPE html>
<html lang="en">
<head>
<meta charset="utf-8">
<title>Hazel Shows Juniper’s Fresh Loft! — Poster</title>
<link rel="stylesheet" href="https://fonts.googleapis.com/css2?family=Montserrat:wght@500;600;700&display=swap">
<style>
  :root {
    --ink: #ffffff;
    --muted: #67625e;
    --accent: #e3262b;
    --track: #6a6764;
    --sky: #dcd8d2;
    --skyline: #6e6660;
    --frame: #8a7454;
    --wall: #4a3e36;
    --hair: #c9a46a;
    --knit: #b7a48c;
    --skin: #c79a80;
    --shadow: #120e0c;
  }
  * { margin: 0; padding: 0; box-sizing: border-box; }
  html, body { width: 790px; height: 1200px; overflow: hidden; background: var(--shadow); }
  body { font-family: "Montserrat", Arial, sans-serif; color: var(--ink); }
  .poster { position: relative; width: 790px; height: 1200px; overflow: hidden; }

  .still { position: absolute; inset: 0; overflow: hidden; }
  .still-window {
    position: absolute; left: 0; top: 0; width: 690px; height: 560px;
    background: linear-gradient(180deg, var(--sky) 0%, #cfcac4 18%, #a39a92 24%, var(--skyline) 34%, #5a514b 48%, #3f3733 62%, #2c2522 100%);
  }
  .still-frame {
    position: absolute; left: 680px; top: 0; width: 40px; height: 640px;
    background: linear-gradient(90deg, #3a2f26 0%, var(--frame) 40%, #d8c39a 55%, #6b5841 100%);
  }
  .still-wall {
    position: absolute; left: 720px; top: 0; width: 70px; height: 1200px;
    background: linear-gradient(180deg, #7a716a 0%, #5d544d 40%, var(--wall) 70%, var(--shadow) 100%);
  }
  .still-sill {
    position: absolute; left: 0; top: 520px; width: 790px; height: 680px;
    background: linear-gradient(180deg, #3b302a 0%, #2a211d 30%, var(--shadow) 100%);
  }
  .still-figures {
    position: absolute; inset: 0;
    background:
      radial-gradient(ellipse 150px 190px at 625px 340px, rgba(199,150,120,0.85) 0%, rgba(150,110,85,0.5) 55%, rgba(0,0,0,0) 100%),
      radial-gradient(ellipse 190px 150px at 610px 230px, rgba(90,62,45,0.9) 0%, rgba(0,0,0,0) 100%),
      radial-gradient(ellipse 170px 330px at 650px 700px, rgba(120,88,80,0.75) 0%, rgba(0,0,0,0) 100%),
      radial-gradient(ellipse 140px 170px at 420px 420px, rgba(210,160,130,0.95) 0%, rgba(180,130,100,0.6) 55%, rgba(0,0,0,0) 100%),
      radial-gradient(ellipse 250px 330px at 360px 470px, rgba(214,178,110,0.95) 0%, rgba(176,138,80,0.75) 55%, rgba(0,0,0,0) 100%),
      radial-gradient(ellipse 330px 300px at 200px 800px, rgba(183,164,140,0.85) 0%, rgba(120,104,86,0.5) 55%, rgba(0,0,0,0) 100%),
      radial-gradient(ellipse 170px 90px at 60px 650px, rgba(200,182,160,0.9) 0%, rgba(0,0,0,0) 100%);
  }
  .scanlines {
    position: absolute; inset: 0;
    background: repeating-linear-gradient(180deg, rgba(0,0,0,0) 0px, rgba(0,0,0,0) 3px, rgba(0,0,0,0.12) 3px, rgba(0,0,0,0.12) 4px);
  }
  .fade {
    position: absolute; left: 0; right: 0; bottom: 0; height: 480px;
    background: linear-gradient(180deg, rgba(0,0,0,0) 0%, rgba(0,0,0,0.35) 40%, rgba(0,0,0,0.7) 100%);
  }

  .studio { position: absolute; top: 62px; left: 0; right: 0; text-align: center; color: var(--muted); text-transform: uppercase; }
  .studio-name { font-weight: 700; font-size: 20px; letter-spacing: 0.3px; }
  .studio-presents { font-weight: 500; font-size: 13px; margin-top: 2px; }

  .billing {
    position: absolute; top: 776px; left: 0; right: 0;
    display: flex; justify-content: center; align-items: center; gap: 12px;
    font-weight: 600; font-size: 18px; text-transform: uppercase;
  }
  .platform { display: flex; align-items: center; gap: 6px; font-size: 18px; }
  .platform-mark { width: 14px; height: 14px; background: var(--accent); }

  .title {
    position: absolute; top: 836px; left: 0; right: 0; text-align: center;
    font-weight: 600; text-transform: uppercase; line-height: 1.05;
  }
  .title span { display: block; }
  .title .l1 { font-size: 68px; }
  .title .l2 { font-size: 68px; }
  .title .l3 { font-size: 56px; }

  .credits { position: absolute; top: 1076px; left: 0; right: 0; text-align: center; text-transform: uppercase; }
  .credit-row { display: flex; justify-content: center; gap: 56px; align-items: baseline; }
  .credit-label { font-size: 9px; font-weight: 500; margin-right: 4px; }
  .credit-name { font-size: 14px; font-weight: 600; }
  .director { margin-top: 8px; font-size: 17px; font-weight: 500; }
  .director b { font-weight: 600; font-size: 19px; }

  .progress { position: absolute; left: 0; top: 1150px; width: 790px; height: 26px; }
</style>
</head>
<body>
<main class="poster">
  <div class="still" role="img" aria-label="Two young women taking a selfie in front of an apartment window overlooking a city skyline at dusk">
    <div class="still-window"></div>
    <div class="still-sill"></div>
    <div class="still-frame"></div>
    <div class="still-wall"></div>
    <div class="still-figures"></div>
  </div>
  <div class="scanlines"></div>
  <div class="fade"></div>

  <header class="studio">
    <div class="studio-name">Nothing’s Amiss Pictures</div>
    <div class="studio-presents">Presents</div>
  </header>

  <div class="billing">
    <span class="star">Marisa Pellwright</span>
    <span class="platform"><span class="platform-mark"></span>StreamNook</span>
    <span class="star">Tamsin Kowalcek</span>
  </div>

  <h1 class="title">
    <span class="l1">Hazel Shows</span>
    <span class="l2">Juniper’s</span>
    <span class="l3">Fresh Loft!</span>
  </h1>

  <section class="credits">
    <div class="credit-row">
      <span><span class="credit-label">Story by</span><span class="credit-name">Jem Ushworth</span></span>
      <span><span class="credit-label">Original music by</span><span class="credit-name">Marisa Pellwright</span></span>
    </div>
    <div class="director">Directed by <b>Dale &amp; Brent Ushworth</b></div>
  </section>

  <svg class="progress" viewBox="0 0 790 26" aria-hidden="true">
    <rect x="0" y="11" width="790" height="4" fill="var(--track)"/>
    <rect x="0" y="10" width="325" height="6" fill="var(--accent)"/>
    <circle cx="325" cy="13" r="12" fill="var(--accent)"/>
  </svg>
</main>
</body>
</html>
```